Edgy rebranded biz cards KRB

We are rebranding our 20 yr old mortgage company with a new logo and would like cards to compliment our new look.

Target Market(s)

potential home buyers or clients for refinance

Industry/Entity Type

Mortgage Brokerage

Contact Information for Business Card

418 W. Lomita Ave #305
Henderson, NV 89152
702.519.4827 o
702-519-4829 f
www.kestrelridgelending,example
nmls 842019
KRB is an equal housing lender

Font styles to use
Sans Serif

Colors
0455a3
3176b5
0393ce
33a6d7

Requirements
Must have
• space for a photo
Nice to have
• One side with the company info and the other with the person's info

```html
<!DOCTYPE html>
<html lang="en">
<head>
<meta charset="utf-8">
<title>Kestrel Ridge Lending – Business Cards</title>
<link rel="stylesheet" href="https://fonts.googleapis.com/css2?family=Source+Sans+3:wght@400;600;700&display=swap">
<style>
  :root {
    --stage: #e3e3e3;
    --card-dark: #2d2d2d;
    --card-light: #f4f4f4;
    --brand-blue: #0a6eb9;
    --brand-gray: #8a8b8d;
    --ink: #2a2a2a;
    --white: #ffffff;
    --photo-top: #c9cbcd;
    --photo-bottom: #2a2f3a;
  }
  * { box-sizing: border-box; margin: 0; padding: 0; }
  html, body {
    width: 1200px; height: 960px; overflow: hidden;
    background: var(--stage);
    font-family: "Source Sans 3", "Source Sans Pro", Arial, sans-serif;
  }
  .canvas { position: relative; width: 1200px; height: 960px; }
  .card { position: absolute; left: 307px; width: 592px; overflow: hidden; }

  /* Front (company) side */
  .card--front { top: 128px; height: 337px; background: var(--card-dark); }
  .brand-lockup {
    position: absolute; left: 0; right: 0; top: 262px;
    display: flex; align-items: center; justify-content: center; gap: 12px;
  }
  .brand-lockup__mark { width: 22px; height: 22px; background: var(--brand-blue); }
  .brand-lockup__name {
    font-weight: 700; font-size: 38px; letter-spacing: 0.5px;
    color: var(--brand-blue); line-height: 1;
  }
  .front-rule {
    position: absolute; top: 355px; height: 3px; background: var(--brand-gray);
  }
  .equal-housing {
    position: absolute; left: 0; right: 0; top: 415px;
    text-align: center; font-size: 15px; color: #e6e6e6;
  }
  .equal-housing__abbr { color: var(--brand-blue); }

  /* Back (person) side */
  .card--back { top: 518px; height: 339px; background: var(--card-light); }
  .back-brand {
    position: absolute; left: 43px; top: 88px;
    display: flex; align-items: center; gap: 9px;
  }
  .back-brand__mark { width: 14px; height: 14px; background: var(--brand-blue); }
  .back-brand__name {
    font-weight: 700; font-size: 23px; color: var(--brand-blue); line-height: 1;
  }
  .back-rule {
    position: absolute; left: 43px; top: 126px; width: 210px; height: 2px;
    background: var(--brand-gray);
  }
  .address {
    position: absolute; left: 43px; top: 169px;
    font-size: 15px; line-height: 19.5px; color: var(--ink);
  }
  .address__license { color: var(--brand-blue); }
  .contact-list {
    position: absolute; left: 43px; top: 238px; list-style: none;
    font-size: 15px; line-height: 19.5px; color: var(--ink);
  }
  .contact-list li { display: flex; align-items: center; gap: 4px; }
  .contact-list svg { width: 14px; height: 14px; flex: none; fill: var(--brand-blue); }

  .portrait {
    position: absolute; left: 410px; top: 41px; width: 143px; height: 180px;
    border: 2px solid var(--brand-blue);
    background: linear-gradient(180deg, var(--photo-top) 0%, #9a9896 45%, var(--photo-bottom) 100%);
  }
  .person {
    position: absolute; right: 41px; top: 236px; text-align: right;
  }
  .person__name {
    font-weight: 600; font-size: 20px; letter-spacing: 0.4px;
    color: var(--brand-blue); line-height: 1.2;
  }
  .person__role { font-size: 14px; color: var(--ink); letter-spacing: 0.3px; margin-top: 1px; }

  .footer-strip {
    position: absolute; left: 0; bottom: 0; width: 340px; height: 14px;
    background: var(--brand-gray);
  }
  .footer-web {
    position: absolute; right: 0; bottom: 0; width: 268px; height: 32px;
    background: var(--brand-blue);
    clip-path: polygon(16px 0, 100% 0, 100% 100%, 0 100%);
    display: flex; align-items: center; justify-content: center;
    padding-left: 14px;
    color: var(--white); font-size: 14px;
  }
</style>
</head>
<body>
<main class="canvas">

  <section class="card card--front" aria-label="Company side">
    <div class="brand-lockup">
      <span class="brand-lockup__mark"></span>
      <span class="brand-lockup__name">KESTREL RIDGE LENDING</span>
    </div>
    <span class="front-rule" style="left:133px; width:88px;"></span>
    <span class="front-rule" style="left:372px; width:88px;"></span>
    <p class="equal-housing"><span class="equal-housing__abbr">KRB</span> is an equal housing lender</p>
  </section>

  <section class="card card--back" aria-label="Personal side">
    <div class="back-brand">
      <span class="back-brand__mark"></span>
      <span class="back-brand__name">KESTREL RIDGE LENDING</span>
    </div>
    <span class="back-rule"></span>

    <p class="address">
      418 W. Lomita Ave #305<br>
      Henderson, NV 89152<br>
      <span class="address__license">nmls 842019</span>
    </p>

    <ul class="contact-list">
      <li>
        <svg viewBox="0 0 24 24" aria-hidden="true"><path d="M6.6 10.8a15.2 15.2 0 0 0 6.6 6.6l2.2-2.2a1 1 0 0 1 1-.25 11.4 11.4 0 0 0 3.6.57 1 1 0 0 1 1 1V20a1 1 0 0 1-1 1A17 17 0 0 1 3 4a1 1 0 0 1 1-1h3.5a1 1 0 0 1 1 1c0 1.25.2 2.45.57 3.57a1 1 0 0 1-.25 1z"/></svg>
        702.519.4827
      </li>
      <li>
        <svg viewBox="0 0 24 24" aria-hidden="true"><path d="M6 2h12v5H6zM3 8h18a1 1 0 0 1 1 1v8h-4v5H6v-5H2V9a1 1 0 0 1 1-1zm5 8v4h8v-4z"/></svg>
        702-519-4829
      </li>
      <li>
        <svg viewBox="0 0 24 24" aria-hidden="true"><path d="M2 5h20v14H2zm2 2v.5l8 5.5 8-5.5V7zm0 2.9V17h16V9.9l-8 5.5z"/></svg>
        daniel@kestrelridgelending,example
      </li>
    </ul>

    <div class="portrait" role="img" aria-label="Portrait photo of the broker"></div>

    <div class="person">
      <p class="person__name">DANIEL WHITFORD</p>
      <p class="person__role">BROKERAGE</p>
    </div>

    <span class="footer-strip"></span>
    <div class="footer-web">www.kestrelridgelending,example</div>
  </section>

</main>
</body>
</html>
```